New Business Card for General Contractor Marketing

Need a business card the is more like a marketing promotion of our services
Must be horizontal orientation, One Sided Only, Max font size, Organize the Services
#1 General Contractor for Realtors
Remodels – Renovations – Repairs
Water & Mold Damage Experts
Painting: Interior/ Exterior
Flooring: Wood / LVT / Carpet
Plumbing: Repairs & Upgrades
Electric: Lights & Energy Efficient Upgrades
Kitchen & Bath Remodels
Fast Inspections Repair Billed Thru Escrow
BrightHarborBuilds.com
555-418-2796

Industry/Entity Type

General Contractor

Contact Information for Business Card

One Sided Only: #1 General Contractor for Realtors Remodels – Renovations – Repairs Water & Mold Damage Experts Painting: Interior/ Exterior Flooring: Wood / LVT / Carpet Plumbing: Repairs & Upgrades Electric: Lights & Energy Efficient Upgrades Kitchen & Bath Remodels Fast Inspections Repair Billed Thru Escrow BrightHarborBuilds.com 555-418-2796

Colors
0054AA
0677BA
7BADD7
CADEEF
E8F1F8

Requirements
Must have
• One Sided Only: #1 General Contractor for Realtors Remodels – Renovations – Repairs Water & Mold Damage Experts Painting: Interior/ Exterior Flooring: Wood / LVT / Carpet Plumbing: Repairs & Upgrades Electric: Lights & Energy Efficient Upgrades Kitchen & Bath Remodels Fast Inspections Repair Billed Thru Escrow BrightHarborBuilds.com 555-418-2796

```html
<!DOCTYPE html>
<html lang="en">
<head>
<meta charset="utf-8">
<title>BrightHarbor Builds – Business Card</title>
<link href="https://fonts.googleapis.com/css2?family=Libre+Baskerville:ital,wght@0,400;0,700;1,400;1,700&family=Roboto:wght@400;500&display=swap" rel="stylesheet">
<style>
  :root {
    --stage: #2e2f31;
    --card: #ffffff;
    --blue-deep: #0a3a7e;
    --blue: #0054aa;
    --blue-bright: #0677ba;
    --orange: #ee7d1c;
    --orange-warm: #f59a16;
    --ink-light: #ffffff;
  }
  * { box-sizing: border-box; margin: 0; padding: 0; }
  html, body {
    width: 1200px; height: 900px; overflow: hidden;
    background: var(--stage);
  }
  .card {
    position: absolute; left: 75px; top: 150px;
    width: 1050px; height: 600px;
    background: var(--card);
    overflow: hidden;
    font-family: "Libre Baskerville", Georgia, serif;
  }
  .card-shapes { position: absolute; inset: 0; }
  .services {
    position: absolute; left: 50px; top: 116px; width: 510px;
    color: var(--ink-light);
  }
  .services-title {
    color: var(--orange);
    font-size: 25px; font-weight: 400;
    letter-spacing: 0.5px; margin-bottom: 8px;
  }
  .services-list { list-style: none; }
  .services-list li {
    font-size: 20px; line-height: 35px;
    padding-left: 20px; white-space: nowrap;
  }
  .services-list li:nth-child(2) { padding-left: 30px; }
  .services-list li:nth-child(3) { padding-left: 40px; }
  .services-list li:nth-child(4) { padding-left: 50px; }
  .services-list li:nth-child(5) { padding-left: 60px; }
  .services-list li:nth-child(6) { padding-left: 70px; }
  .brand {
    position: absolute; left: 600px; top: 268px; width: 430px;
    text-align: center;
  }
  .brand-name {
    display: flex; align-items: center; justify-content: center; gap: 12px;
    color: var(--blue); font-size: 34px; font-weight: 700;
  }
  .brand-dot {
    width: 22px; height: 22px; background: var(--orange); border-radius: 50%;
  }
  .brand-role {
    margin-top: 12px;
    color: var(--blue); font-size: 17px; letter-spacing: 0.6px;
    text-transform: uppercase;
    border-bottom: 1.5px solid var(--orange); padding-bottom: 4px;
    display: inline-block;
  }
  .brand-tagline {
    margin-top: 4px;
    font-family: "Roboto", Arial, sans-serif;
    color: var(--orange); font-size: 14px;
  }
  .escrow-note {
    position: absolute; left: 50px; top: 470px;
    color: var(--orange); font-size: 23px; font-style: italic; font-weight: 700;
    white-space: nowrap;
  }
  .phone {
    position: absolute; left: 62px; top: 532px;
    display: flex; align-items: center; gap: 14px;
    color: var(--ink-light);
    font-family: "Roboto", Arial, sans-serif; font-size: 46px; font-weight: 500;
  }
  .phone svg { width: 40px; height: 40px; }
  .website {
    position: absolute; left: 650px; top: 440px; width: 400px;
    text-align: center;
    color: var(--blue-deep); font-size: 29px; font-weight: 700;
  }
</style>
</head>
<body>
<main class="card">
  <svg class="card-shapes" width="1050" height="600" viewBox="0 0 1050 600" aria-hidden="true">
    <defs>
      <linearGradient id="panel-blue" x1="0" y1="1" x2="1" y2="0">
        <stop offset="0" stop-color="#0a3470"/>
        <stop offset="1" stop-color="#0c52a6"/>
      </linearGradient>
      <linearGradient id="band-orange" x1="0" y1="0" x2="1" y2="0">
        <stop offset="0" stop-color="#e4701c"/>
        <stop offset="1" stop-color="#f7a114"/>
      </linearGradient>
      <linearGradient id="photo-tones" x1="0" y1="0" x2="1" y2="1">
        <stop offset="0" stop-color="#c9ccd2"/>
        <stop offset="0.45" stop-color="#9a6a3e"/>
        <stop offset="0.75" stop-color="#d9b57a"/>
        <stop offset="1" stop-color="#e9e9ea"/>
      </linearGradient>
    </defs>
    <polyline class="panel-frame" points="0,68 478,68 584,162 584,412 0,412" fill="none" stroke="var(--orange)" stroke-width="2"/>
    <polygon class="services-panel" points="0,80 470,80 570,168 570,400 0,400" fill="url(#panel-blue)"/>
    <polygon class="contact-band" points="0,520 612,520 662,388 1050,388 1050,600 0,600" fill="url(#band-orange)"/>
    <line x1="0" y1="443" x2="640" y2="443" stroke="var(--orange)" stroke-width="2"/>
    <polygon class="escrow-band" points="0,452 650,452 622,522 0,522" fill="var(--blue)"/>
    <polygon points="580,18 1030,18 1030,222 702,262 580,122" fill="none" stroke="var(--orange)" stroke-width="2"/>
    <polygon role="img" aria-label="Photo collage of renovated kitchens with wood cabinets and white counters" points="594,28 1030,28 1030,212 706,250 594,120" fill="url(#photo-tones)"/>
  </svg>

  <section class="services">
    <h2 class="services-title">OUR SERVICES</h2>
    <ul class="services-list">
      <li>Water &amp; Mold Damage Experts</li>
      <li>Painting: Interior/ Exterior</li>
      <li>Flooring: Wood / LVT / Carpet</li>
      <li>Plumbing: Repairs &amp; Upgrades</li>
      <li>Electric: Lights &amp; Energy Efficient Upgrades</li>
      <li>Kitchen &amp; Bath Remodels</li>
    </ul>
  </section>

  <div class="brand">
    <div class="brand-name"><span class="brand-dot"></span>BrightHarbor Builds</div>
    <div class="brand-role">General Contractor for Realtors</div>
    <div class="brand-tagline">Remodels – Renovations – Repairs</div>
  </div>

  <p class="escrow-note">Fast Inspections Repair Billed Thru Escrow</p>

  <div class="phone">
    <svg viewBox="0 0 24 24" aria-hidden="true"><path fill="#fff" d="M6.6 10.8a15.1 15.1 0 0 0 6.6 6.6l2.2-2.2a1 1 0 0 1 1-.25 11.4 11.4 0 0 0 3.6.57 1 1 0 0 1 1 1V20a1 1 0 0 1-1 1A17 17 0 0 1 3 4a1 1 0 0 1 1-1h3.5a1 1 0 0 1 1 1c0 1.250.2 2.460.57 3.6a1 1 0 0 1-.25 1z"/></svg>
    <span>555-418-2796</span>
  </div>

  <p class="website">BrightHarborBuilds.com</p>
</main>
</body>
</html>
```